Service Menu refresh 2018 Update of menu pricing

We currently have service menus as attached. We will be updating our look via our homepage image, our service menu and our in-house beverage and treatment menu.
We are a natural and sustainable hair salon group and moving more towards head spa which consists of treatments, beauty, tanning as well as your traditional hair services. Our imagery needs to reflect our efforts in spa treatments in the hair and scalp area and use natural materials and colours reflecting sustainability.
Elvu is the brand we stock and promote.

Target Market(s)

Men or women interesting in personal maintenance with natural and organic products and using sustainable practises

Industry/Entity Type

Hair And Beauty

Font styles to use
Sans Serif
Other font styles liked:
• Arial or Helvetica

Colors
9acb3c
abd037
cadf82
ffffff

Requirements
Must have
• Name on the front cover, locations on back cover
Nice to have
• Prestige feel, reflect male and female clients
Should not have
• Bold artificial writing or any type of cartoon images.
• Same images as existing menu.

```html
<!DOCTYPE html>
<html lang="en">
<head>
<meta charset="utf-8">
<title>Purely Verdant Hair Studios – Service Menu</title>
<link href="https://fonts.googleapis.com/css2?family=Arimo:ital,wght@0,400;0,700;1,400&family=Archivo+Black&family=Great+Vibes&display=swap" rel="stylesheet">
<style>
:root{
  --bg:#dcdedb;
  --green:#9acb3c;
  --lime:#abd037;
  --pale:#cadf82;
  --tint:#e9f2d8;
  --white:#ffffff;
  --ink:#5b5b5b;
  --ink-dark:#3a3a3a;
}
*{box-sizing:border-box;margin:0;padding:0}
html,body{width:795px;height:1200px;overflow:hidden;background:var(--bg)}
body{position:relative;font-family:Arimo,Arial,sans-serif;color:var(--ink)}

/* ---------- front cover ---------- */
.front{position:absolute;left:62px;top:50px;width:667px;height:502px;background:var(--white);overflow:hidden}
.hero-photo{position:absolute;left:0;top:0;width:667px;height:336px;
  background:linear-gradient(100deg,#3d3a30 0%,#6b6253 30%,#4a4a3a 52%,#2f4a2c 70%,#1f3a22 100%)}
.hero-band{position:absolute;left:0;top:318px;width:667px;height:56px}
.brand-front{position:absolute;left:178px;top:70px;color:var(--white);font-size:22px;font-weight:400;letter-spacing:.2px;line-height:1.1}
.hero-quote{position:absolute;left:35px;top:256px;width:420px;color:var(--white);font-family:"Great Vibes",cursive;font-size:26px;line-height:22px}
.hero-quote span{display:block;padding-left:65px}

.location{position:absolute;width:220px}
.location h3{font-family:"Archivo Black",Arial,sans-serif;font-size:12.5px;color:var(--green);letter-spacing:.3px;line-height:14px;display:flex;align-items:center;gap:5px}
.location h3::before{content:"";width:8px;height:8px;border-radius:50%;background:var(--green)}
.location p{font-size:6.6px;line-height:8.6px;color:var(--ink);padding-left:16px;margin-top:2px}
.web-box{position:absolute;left:436px;top:456px;width:214px;height:28px;border:1px solid #c9c9c9;border-top:none;background:var(--white);text-align:center}
.web-box .lead{font-size:10px;color:var(--ink);margin-top:-6px;background:var(--white);display:inline-block;padding:0 3px}
.web-box .url{font-size:10.5px;font-weight:700;color:var(--green);letter-spacing:.3px}

/* ---------- back cover / price list ---------- */
.back{position:absolute;left:58px;top:578px;width:680px;height:478px;background:var(--white);overflow:hidden}
.edge{position:absolute;left:0;top:0;width:110px;height:478px}
.col-heading{position:absolute;font-family:"Archivo Black",Arial,sans-serif;font-size:15px;color:var(--green);letter-spacing:.3px;display:flex;align-items:center;gap:4px;line-height:16px}
.col-heading::before{content:"";width:9px;height:9px;border-radius:50%;background:var(--green)}
.price-box{position:absolute;background:var(--tint);border-radius:0 14px 0 14px;padding:6px 0 6px 13px}
.group+.group{margin-top:13px}
.group h4{font-family:Arimo,Arial,sans-serif;font-weight:700;font-size:10.6px;color:var(--green);letter-spacing:.4px;line-height:13px}
.group h4 small{display:block;font-size:6.4px;font-weight:400;color:var(--ink);letter-spacing:0;line-height:9px}
.row{display:flex;font-size:9.4px;line-height:13.6px}
.row .item{width:110px}
.foot-left{position:absolute;left:0;top:426px;width:278px;height:52px;background:var(--green);border-radius:0 30px 0 0;
  font-style:italic;font-size:8.8px;line-height:11px;color:var(--white);text-align:center;padding:12px 16px 0 24px}
.foot-right{position:absolute;left:472px;top:416px;width:208px;height:52px;background:linear-gradient(90deg,var(--lime),var(--green));border-radius:30px 0 0 0;
  font-size:8.6px;line-height:11.4px;color:var(--white);padding:10px 0 0 34px}

/* ---------- standalone name ---------- */
.brand-mark{position:absolute;left:0;top:1112px;width:795px;text-align:center;font-size:26px;color:var(--ink-dark);letter-spacing:.2px}
</style>
</head>
<body>

<section class="front">
  <div class="hero-photo" role="img" aria-label="Photograph of a woman in a sun hat and sunglasses in a greenhouse, framed on the right by dense tropical foliage illustration"></div>
  <svg class="hero-band" viewBox="0 0 667 56" preserveAspectRatio="none" aria-hidden="true">
    <defs>
      <linearGradient id="band" x1="0" x2="1">
        <stop offset="0" stop-color="#c6dc2a"/><stop offset=".5" stop-color="#abd037"/><stop offset="1" stop-color="#9acb3c"/>
      </linearGradient>
    </defs>
    <path d="M0 6 C220 2 450 6 667 0 L667 56 L0 56Z" fill="#b5b7b4"/>
    <path d="M0 10 C220 6 450 10 667 4 L667 38 C450 50 220 48 0 44Z" fill="url(#band)"/>
    <path d="M0 44 C220 48 450 50 667 38 L667 44 C450 56 220 54 0 50Z" fill="#9e9f9c"/>
    <path d="M0 50 C220 54 450 56 667 44 L667 56 L0 56Z" fill="#ffffff"/>
  </svg>
  <div class="brand-front">purelyverdant hair studios</div>
  <p class="hero-quote">"Living a more natural and organic life is a<span>philosophy not just a product certification"</span></p>

  <div class="location" style="left:40px;top:390px">
    <h3>BAYVIEW</h3>
    <p>Shop 104 Parkway Bayview, Harbour Rd, Bayview<br>+61 (07) 3000 1101<br>bayview@verdantstudios.example</p>
  </div>
  <div class="location" style="left:259px;top:390px">
    <h3>HILLCREST</h3>
    <p>Shop 212 Parkway Hillcrest, Summit Road, Hillcrest<br>+61 (07) 3000 1102<br>hillcrest@verdantstudios.example</p>
  </div>
  <div class="location" style="left:489px;top:390px">
    <h3>NGMC</h3>
    <p>Northgate Medical Centre<br>Fernleigh St, Northgate QLD 4000<br>+61 (07) 3000 1103<br>ngmc@verdantstudios.example</p>
  </div>
  <div class="location" style="left:40px;top:443px">
    <h3>LAKESIDE</h3>
    <p>Shop 1120 Parkway Lakeside, Shore St Lakeside<br>+61 (07) 3000 1104<br>lakeside@verdantstudios.example</p>
  </div>
  <div class="location" style="left:259px;top:443px">
    <h3>RIVERBEND</h3>
    <p>Shop 3010 Riverbend Shopping Centre,<br>Willow Rd Riverbend<br>+61 (07) 3000 1105<br>riverbend@verdantstudios.example</p>
  </div>
  <div class="web-box">
    <div class="lead">for more information visit our website</div>
    <div class="url">www.verdantstudios.example</div>
  </div>
</section>

<section class="back">
  <svg class="edge" viewBox="0 0 110 478" aria-hidden="true">
    <defs>
      <linearGradient id="edgeGreen" x1="0" x2="1" y1="0" y2="1">
        <stop offset="0" stop-color="#c6dc2a"/><stop offset="1" stop-color="#9acb3c"/>
      </linearGradient>
    </defs>
    <path d="M0 0 H78 C60 120 58 300 84 478 H0Z" fill="url(#edgeGreen)"/>
    <path d="M78 0 H92 C74 120 72 300 98 478 H84 C58 300 60 120 78 0Z" fill="#c9cbc8"/>
    <path d="M20 0 C10 150 40 330 12 478" stroke="#b8d23a" stroke-width="14" fill="none" opacity=".6"/>
  </svg>

  <div class="col-heading" style="left:100px;top:16px">CUT &amp; BLOW-DRY</div>
  <div class="price-box" style="left:102px;top:38px;width:158px;height:372px">
    <div class="group"><h4>LADIES</h4>
      <div class="row"><span class="item">Short</span>$77</div>
      <div class="row"><span class="item">Medium</span>$88</div>
      <div class="row"><span class="item">Long</span>$99</div>
      <div class="row"><span class="item">Extra long</span>$110</div>
    </div>
    <div class="group"><h4>FRINGE</h4>
      <div class="row"><span class="item">Trim</span>$25</div>
      <div class="row"><span class="item">Restyle</span>$35</div>
    </div>
    <div class="group"><h4>MENS</h4>
      <div class="row"><span class="item">Single Blade Clipper</span>$28</div>
      <div class="row"><span class="item">Style Cut</span>$42</div>
    </div>
    <div class="group"><h4>CHILDREN</h4>
      <div class="row"><span class="item">10 and Under</span>$24</div>
      <div class="row"><span class="item">11-16 Male</span>$32</div>
      <div class="row"><span class="item">11-16 Female</span>$48</div>
      <div class="row"><span class="item">add a wash</span>$5</div>
    </div>
    <div class="group"><h4>BLOWDRY</h4>
      <div class="row"><span class="item">Short</span>$47</div>
      <div class="row"><span class="item">Medium</span>$57</div>
      <div class="row"><span class="item">Long</span>$67</div>
      <div class="row"><span class="item">Extra long</span>$77</div>
      <div class="row"><span class="item">Shampoo &amp; Dry Off</span>$25</div>
    </div>
  </div>

  <div class="col-heading" style="left:300px;top:16px">FOILS</div>
  <div class="price-box" style="left:304px;top:36px;width:154px;height:310px">
    <div class="group"><h4>SINGLE *</h4>
      <div class="row"><span class="item">Short</span>$11</div>
      <div class="row"><span class="item">Med</span>$13</div>
      <div class="row"><span class="item">Long</span>$17</div>
      <div class="row"><span class="item">Extra Long</span>$22</div>
    </div>
    <div class="group"><h4>1/4 HEAD</h4>
      <div class="row"><span class="item">Short</span>$135</div>
      <div class="row"><span class="item">Med</span>$155</div>
      <div class="row"><span class="item">Long</span>$175</div>
      <div class="row"><span class="item">Extra Long</span>$195</div>
    </div>
    <div class="group"><h4>1/2 HEAD</h4>
      <div class="row"><span class="item">Short</span>$185</div>
      <div class="row"><span class="item">Med</span>$205</div>
      <div class="row"><span class="item">Long</span>$235</div>
      <div class="row"><span class="item">Extra Long</span>$265</div>
    </div>
    <div class="group"><h4>FULL HEAD</h4>
      <div class="row"><span class="item">Short</span>$235</div>
      <div class="row"><span class="item">Med</span>$265</div>
      <div class="row"><span class="item">Long</span>$315</div>
      <div class="row"><span class="item">Extra Long</span>$355</div>
    </div>
  </div>

  <div class="col-heading" style="left:300px;top:352px">TREATMENTS</div>
  <div class="price-box" style="left:304px;top:373px;width:154px;height:32px;padding-top:4px;border-radius:0">
    <div class="row" style="line-height:12px"><span class="item">Deep Treatment</span>$35</div>
    <div class="row" style="line-height:12px"><span class="item">Head.Spa Ritual</span>$65</div>
  </div>

  <div class="col-heading" style="left:300px;top:409px">UPSTYLE</div>
  <div class="price-box" style="left:304px;top:431px;width:154px;height:32px;padding-top:4px;border-radius:0">
    <div class="row" style="line-height:12px"><span class="item">45 (minutes)</span>$85</div>
    <div class="row" style="line-height:12px"><span class="item">60 (minutes)</span>$120</div>
  </div>

  <div class="col-heading" style="left:491px;top:16px">COLOUR</div>
  <div class="price-box" style="left:492px;top:40px;width:168px;height:362px">
    <div class="group"><h4>H COLOUR</h4>
      <div class="row"><span class="item">Regrowth</span>$83</div>
      <div class="row"><span class="item">Short</span>$125</div>
      <div class="row"><span class="item">Med</span>$145</div>
      <div class="row"><span class="item">Long</span>$165</div>
      <div class="row"><span class="item">X-Long</span>$185</div>
    </div>
    <div class="group"><h4>H COLOUR</h4>
      <div class="row"><span class="item">Regrowth</span>$99</div>
      <div class="row"><span class="item">Short</span>$155</div>
      <div class="row"><span class="item">Med</span>$175</div>
      <div class="row"><span class="item">Long</span>$195</div>
      <div class="row"><span class="item">X-Long</span>$205</div>
    </div>
    <div class="group"><h4>REGROWTH LIGHTENING<small>(INCLUDES COLOUR MATCH &amp; TONING)</small></h4>
      <div class="row"><span class="item">Short</span>$165</div>
      <div class="row"><span class="item">Med</span>$189</div>
      <div class="row"><span class="item">Long</span>$209</div>
      <div class="row"><span class="item">Extra Long</span>$229</div>
    </div>
    <div class="group"><h4>BALAYAGE/OMBRE<small>(INCLUDES COLOUR MATCH &amp; TONING)</small></h4>
      <div class="row"><span class="item">Med</span>$275</div>
      <div class="row"><span class="item">Long</span>$375</div>
      <div class="row"><span class="item">Extra Long</span>$475</div>
    </div>
  </div>

  <div class="foot-left">*Pricing is indicative of average products used and time taken for each service. You will always receive a firm price after your consultation.</div>
  <div class="foot-right">* Includes colour match &amp; toner<br>*Minimum 6 foils without colour<br>*Minimum charge on Sunday is $40</div>
</section>

<div class="brand-mark">purelyverdant hair studios</div>

</body>
</html>
```